Geschäftspapiere für ein Hotel
Zielgruppe
Wir sind ein Hotel in den Tiroler Bergen im höchsten Wintersportort Österreichs - in Kühtai.
Aufgabenstellung
Wir hättn gerne neue Kuverts...
einmal im Format C6/5 (ohne Adress-Fenster)
und dann noch im Format C4 und
dann noch Briefpapier
Wir haben neben unserem Hotel noch ein kleines Häuschen mit Ferienwohnungen...das Logo ist auch bei den Dateien.
Noch dazu haben wir ein Restaurant im Haus....Logo ist auch dabei.
Noch dazu ist ein Foto bei den Dateien welches in Österreich auf jedem Kuvert sein muss.
Einige Bilder von unserem Haus und Wellness-Bereich hab ich auch noch hinzugefügt.
Freue mich auf viele Design-Vorschläge
Unter folgendem Link werde ich heute nachmittag noch einige Fotos uploaden:
https://ablage.wolkenfach.example/ordner/7qpTzr3MvLx09KbNe2hYsW4dRfUjaC8Po?zugang=offen

```html
<!DOCTYPE html>
<html lang="de">
<head>
<meta charset="utf-8">
<title>Almfels Hotel – Geschäftspapiere</title>
<link href="https://fonts.googleapis.com/css2?family=Cormorant+Garamond:wght@600&family=Open+Sans:wght@400;600&display=swap" rel="stylesheet">
<style>
  :root{
    --bg:#ffffff;
    --paper:#ffffff;
    --brown:#5a3a26;
    --ink:#6b6b6b;
    --mist-1:#d9dde3;
    --mist-2:#eef0f3;
    --alpine:#7d9cc4;
    --snow:#c9d6e6;
    --pool:#2c4f9a;
    --wood:#7a4a2a;
    --room:#b0713e;
  }
  *{box-sizing:border-box;margin:0;padding:0}
  html,body{width:1200px;height:1200px;overflow:hidden;background:var(--bg)}
  body{position:relative;font-family:"Open Sans",sans-serif}
  .sheet{position:absolute;background:var(--paper);box-shadow:2px 3px 6px rgba(0,0,0,.28);overflow:hidden}
  .letterhead{left:24px;top:221px;width:437px;height:619px}
  .envelope-c4{left:494px;top:221px;width:682px;height:418px}
  .envelope-c65{left:494px;top:737px;width:480px;height:236px}
  .mountain-haze{position:absolute;left:0;top:0;width:100%;
    background:linear-gradient(180deg,var(--mist-1) 0%,var(--mist-2) 55%,rgba(255,255,255,0) 100%)}
  .letterhead .mountain-haze{height:200px}
  .envelope-c4 .mountain-haze{height:220px}
  .envelope-c65 .mountain-haze{height:110px}
  .brand{position:absolute;text-align:center;color:var(--brown);white-space:nowrap}
  .brand-name{font-family:"Cormorant Garamond",serif;font-weight:600;line-height:1;letter-spacing:.03em;display:block}
  .brand-tag{font-family:"Cormorant Garamond",serif;font-weight:600;display:block;letter-spacing:.3em;color:var(--brown)}
  .letterhead .brand{right:24px;top:24px;width:110px}
  .letterhead .brand-name{font-size:15px}
  .letterhead .brand-tag{font-size:5.5px;margin-top:3px}
  .envelope-c4 .brand{left:40px;top:280px;width:150px}
  .envelope-c4 .brand-name{font-size:19px}
  .envelope-c4 .brand-tag{font-size:6.5px;margin-top:4px}
  .envelope-c65 .brand{left:34px;top:102px;width:110px}
  .envelope-c65 .brand-name{font-size:13px}
  .envelope-c65 .brand-tag{font-size:5px;margin-top:3px}
  .contact{position:absolute;right:28px;top:62px;width:102px;font-size:5.5px;line-height:8px;color:var(--ink)}
  .contact p{margin:0}
  .contact .gap{height:6px}
  .contact .row{display:flex;align-items:center;gap:4px}
  .contact svg{width:7px;height:7px;flex:none}
  .photo-strip{position:absolute;left:0;width:100%;display:flex;gap:3px;
    border-top:3px solid var(--brown);border-bottom:3px solid var(--brown);padding:4px 0;background:var(--paper)}
  .photo-strip .photo{flex:1}
  .letterhead .photo-strip{top:530px;height:66px}
  .envelope-c4 .photo-strip{top:345px;height:72px}
  .envelope-c65 .photo-strip{top:155px;height:68px}
  .photo.peaks{background:linear-gradient(180deg,var(--alpine),var(--snow) 60%,#f2f5f9)}
  .photo.hotel{background:linear-gradient(180deg,#5f8fd0,#dfe6ee 55%,#b8bec6)}
  .photo.pool{background:linear-gradient(180deg,#1e2d6b,var(--pool) 50%,#5a8ed0)}
  .photo.dining{background:linear-gradient(180deg,#3a2414,var(--wood) 55%,#c79560)}
  .photo.suite{background:linear-gradient(180deg,#6e3a20,var(--room) 50%,#f1e3d2)}
  .postage{position:absolute;border:1px solid #999;background:#fff;font-size:5px;line-height:7px;color:#444}
  .envelope-c4 .postage{right:40px;top:18px;width:150px;height:72px;padding:6px 8px}
  .envelope-c65 .postage{right:24px;top:14px;width:112px;height:54px;padding:4px 6px;font-size:4px;line-height:5.5px}
  .postage-head{display:flex;align-items:center;gap:6px;margin-bottom:6px}
  .postage-mark{width:18px;height:12px;background:#d8d8d8}
  .envelope-c65 .postage-mark{width:14px;height:9px}
  .postage-label{font-weight:600;color:#222}
</style>
</head>
<body>

<section class="sheet letterhead" aria-label="Briefpapier">
  <div class="mountain-haze" role="img" aria-label="Verblasste Winterberglandschaft"></div>
  <div class="brand"><span class="brand-name">Almfels Hotel</span><span class="brand-tag">HOTEL · TIROL</span></div>
  <div class="contact">
    <p>Almfels Hotel</p>
    <p>Firnweg 14</p>
    <p>9990 Schneetal</p>
    <div class="gap"></div>
    <div class="row"><svg viewBox="0 0 10 10"><circle cx="5" cy="5" r="4.5" fill="none" stroke="#5a3a26"/><path d="M3.4 3c.3 1.6 1.6 3.3 3.4 3.8l.5-.8-.9-.6-.5.4C5 5.3 4.6 4.8 4.4 4.2l.5-.4-.5-1z" fill="#5a3a26"/></svg><p>+43 000 0000</p></div>
    <div class="row"><svg viewBox="0 0 10 10"><circle cx="5" cy="5" r="4.5" fill="none" stroke="#5a3a26"/><rect x="2.8" y="3.5" width="4.4" height="3" fill="none" stroke="#5a3a26" stroke-width=".7"/><path d="M2.8 3.5l2.2 1.7 2.2-1.7" fill="none" stroke="#5a3a26" stroke-width=".7"/></svg><p>info@almfels.example</p></div>
    <div class="row"><svg viewBox="0 0 10 10"><circle cx="5" cy="5" r="4.5" fill="none" stroke="#5a3a26"/><circle cx="5" cy="5" r="2.3" fill="none" stroke="#5a3a26" stroke-width=".7"/><path d="M2.7 5h4.6M5 2.7v4.6" stroke="#5a3a26" stroke-width=".6"/></svg><p>www.almfels.example</p></div>
  </div>
  <div class="photo-strip">
    <div class="photo peaks" role="img" aria-label="Verschneite Berggipfel"></div>
    <div class="photo hotel" role="img" aria-label="Hotel im Winter"></div>
    <div class="photo pool" role="img" aria-label="Wellness-Schwimmbad"></div>
    <div class="photo dining" role="img" aria-label="Restaurant mit Holzstube"></div>
    <div class="photo suite" role="img" aria-label="Hotelzimmer"></div>
  </div>
</section>

<section class="sheet envelope-c4" aria-label="Kuvert C4">
  <div class="mountain-haze" role="img" aria-label="Verblasste Winterberglandschaft"></div>
  <div class="postage">
    <div class="postage-head"><span class="postage-mark"></span><span class="postage-label">Entgelt bezahlt</span></div>
    <p>Bei Unzustellbarkeit zurück</p>
    <p>9990 Schneetal</p>
    <p>Österreich</p>
  </div>
  <div class="brand"><span class="brand-name">Almfels Hotel</span><span class="brand-tag">HOTEL · TIROL</span></div>
  <div class="photo-strip">
    <div class="photo peaks" role="img" aria-label="Verschneite Berggipfel"></div>
    <div class="photo hotel" role="img" aria-label="Hotel im Winter"></div>
    <div class="photo pool" role="img" aria-label="Wellness-Schwimmbad"></div>
    <div class="photo dining" role="img" aria-label="Restaurant mit Holzstube"></div>
    <div class="photo suite" role="img" aria-label="Hotelzimmer"></div>
  </div>
</section>

<section class="sheet envelope-c65" aria-label="Kuvert C6/5">
  <div class="mountain-haze" role="img" aria-label="Verblasste Winterberglandschaft"></div>
  <div class="postage">
    <div class="postage-head"><span class="postage-mark"></span><span class="postage-label">Entgelt bezahlt</span></div>
    <p>Bei Unzustellbarkeit zurück</p>
    <p>9990 Schneetal</p>
    <p>Österreich</p>
  </div>
  <div class="brand"><span class="brand-name">Almfels Hotel</span><span class="brand-tag">HOTEL · TIROL</span></div>
  <div class="photo-strip">
    <div class="photo peaks" role="img" aria-label="Verschneite Berggipfel"></div>
    <div class="photo hotel" role="img" aria-label="Hotel im Winter"></div>
    <div class="photo pool" role="img" aria-label="Wellness-Schwimmbad"></div>
    <div class="photo dining" role="img" aria-label="Restaurant mit Holzstube"></div>
    <div class="photo suite" role="img" aria-label="Hotelzimmer"></div>
  </div>
</section>

</body>
</html>
```